Aged Care Home - TP

We need a website design for a homepage and a content page for an aged care home in Brisbane. I have attached a detailed design/content brief and their logo to be used in concepts. Also bear in mind this design will be skinned for Dot Net Nuke 4.8.2 so design needs to be used on this content management system.

The following elements are required in the design:

• Phone number will be featured in banner on each page 07 5281 6372

• An area for a large flash banner of rotating images on homepage

• Images need to reflect credibility, professionalism and caring (just use some example images for now as we’ll need to source some)

• Large logo in banner as well

• Some icons on homepage to include:

• Download Application Form

• Admission Kit

• Contact Us

```html
<!DOCTYPE html>
<html lang="en">
<head>
<meta charset="utf-8">
<title>The Tom Parker Home</title>
<link href="https://fonts.googleapis.com/css2?family=Cabin:wght@400;500&display=swap" rel="stylesheet">
<style>
  :root {
    --sky-edge: #b2e0f2;
    --sky-mid: #e4f4fa;
    --brand-blue: #1d22a8;
    --navy: #0f1a6e;
    --tab-dark-top: #07095a;
    --tab-dark-bottom: #1a1f8e;
    --tab-light-top: #10129a;
    --tab-light-bottom: #2a3fc4;
    --green-top: #8fd43a;
    --green-bottom: #6bbf06;
    --body-text: #1a1a1a;
    --rule: #1a1f8e;
  }
  html, body {
    margin: 0;
    padding: 0;
    overflow: hidden;
  }
  body {
    width: 1200px;
    height: 1000px;
    position: relative;
    font-family: "Cabin", "Gill Sans", sans-serif;
    background: linear-gradient(90deg, var(--sky-edge) 0%, var(--sky-mid) 50%, var(--sky-edge) 100%);
  }
  .brand {
    position: absolute;
    left: 151px;
    top: 104px;
  }
  .brand-dot {
    position: absolute;
    left: 0;
    top: 40px;
    width: 46px;
    height: 46px;
    border-radius: 50%;
    background: var(--brand-blue);
    opacity: .75;
  }
  .brand-name {
    position: absolute;
    left: 58px;
    top: 0;
    margin: 0;
    font-weight: 400;
    color: var(--brand-blue);
    white-space: nowrap;
    line-height: 1;
  }
  .brand-name .article {
    display: block;
    font-size: 12px;
    margin-bottom: 2px;
  }
  .brand-name .title {
    font-size: 24.5px;
    letter-spacing: .2px;
  }
  .call-us {
    position: absolute;
    left: 270px;
    top: 160px;
    margin: 0;
    color: var(--navy);
    font-size: 18.5px;
    line-height: 25px;
    font-weight: 500;
  }
  .nav-tab {
    position: absolute;
    right: 149px;
    display: flex;
    align-items: center;
    justify-content: space-around;
    border-radius: 14px 14px 0 0;
    font-size: 17px;
    letter-spacing: .4px;
  }
  .nav-tab a {
    color: #fff;
    text-decoration: none;
  }
  .nav-primary {
    top: 139px;
    left: 503px;
    height: 46px;
    background: linear-gradient(180deg, var(--tab-dark-top), var(--tab-dark-bottom));
  }
  .nav-secondary {
    top: 182px;
    left: 463px;
    height: 50px;
    background: linear-gradient(180deg, var(--tab-light-top), var(--tab-light-bottom));
  }
  .hero {
    position: absolute;
    left: 151px;
    top: 232px;
    width: 900px;
    height: 300px;
    background: linear-gradient(90deg, #6b5a3c 0%, #8a7a55 20%, #a9c77a 42%, #5f9b3a 60%, #7fb24c 78%, #4f7e2a 100%);
  }
  .quick-links {
    position: absolute;
    left: 151px;
    top: 577px;
    width: 251px;
  }
  .quick-link {
    display: flex;
    align-items: center;
    justify-content: center;
    text-align: center;
    height: 55px;
    margin-bottom: 23px;
    border-radius: 9px;
    background: linear-gradient(180deg, var(--green-top) 0%, var(--green-bottom) 45%, var(--green-bottom) 100%);
    color: #fff;
    font-size: 18px;
    line-height: 20px;
    letter-spacing: .4px;
    text-decoration: none;
  }
  .intro {
    position: absolute;
    left: 446px;
    top: 566px;
    width: 610px;
    color: var(--body-text);
    font-size: 18px;
    line-height: 33px;
    letter-spacing: .2px;
  }
  .intro p {
    margin: 0 0 33px;
  }
  .footer-rule {
    position: absolute;
    left: 151px;
    top: 852px;
    width: 900px;
    height: 2px;
    background: var(--rule);
  }
</style>
</head>
<body>
  <header class="brand">
    <span class="brand-dot"></span>
    <h1 class="brand-name"><span class="article">the</span><span class="title">TOM PARKER HOME</span></h1>
  </header>
  <p class="call-us">Call Us Today:<br>07 5281 6372</p>

  <nav class="nav-tab nav-primary">
    <a href="#">Home</a>
    <a href="#">About Us</a>
    <a href="#">Accommodation</a>
    <a href="#">Contact Us</a>
  </nav>
  <nav class="nav-tab nav-secondary">
    <a href="#">Financial Info</a>
    <a href="#">Philosophy of Care</a>
    <a href="#">Sign up for newsletter</a>
  </nav>

  <div class="hero" role="img" aria-label="Rotating banner photos: a young woman hugging an older woman by a tree, and an older couple sitting on a park bench among trees"></div>

  <div class="quick-links">
    <a class="quick-link" href="#">Download<br>Application Form</a>
    <a class="quick-link" href="#">Admission Kit</a>
    <a class="quick-link" href="#">Contact Us</a>
  </div>

  <section class="intro">
    <p>We are an Aged Care Facility that has been providing quality care and accommodation to the Brisbane community for over twenty years.</p>
    <p>From this site you can learn more about us, find out all the types of accommodation available, what our Philosophy of Care is, send a message to a resident, contact us to request more information or download a brochure or an application form.</p>
  </section>

  <div class="footer-rule"></div>
</body>
</html>
```